Specialized Personal Trainer Needs a Business Card Design

I need a business card design for my personal training business called Tall Oak Fitness. I have my Human Kinetics degree in Exercise Science from the Halvern Ridge University as well as an extra certification from NBEP (National Board of Exercise Practice). I work as a Cardiac Rehab Exercise Specialist and personal trainer giving specialized exercise prescriptions to those that have different heart conditions as well as work with the general population in weight loss, strength and conditioning, getting/staying fit.
Updates

I decided that I wanted a logo (as I did not have one before I submitted my project for a business card) so I am submitting a project to get a logo done and then I will decide on a business card, hopefully being able to use one of the designs already submitted.  My apologies for doing this backwards.  I am new to this so I appreciate your patience.

Thank you.

Hi, I have just created a project for a logo design (I realized I needed a logo and I should've done that first..oops!), please feel free to participate.  Once I receive a logo I like I will finalize my business card project and hopefully incorporate it into one of your business card designs. 

Thank you!

Target Market(s)

Business professionals

Industry/Entity Type

Personal Trainer

Requirements
Must have
• My name with my info:
Celia R. Dunhill (BHK)
NBEP Certified Clinical Exercise Specialist & Personal Trainer
celia.dunhill@talloakfitness.example
Cell: 604-358-4170

Please make it double sided.
Nice to have
• An image that represents cardiac and general fitness training.

```html
<!DOCTYPE html>
<html lang="en">
<head>
<meta charset="utf-8">
<title>Tall Oak Fitness – Business Card Concepts</title>
<link rel="stylesheet" href="https://fonts.googleapis.com/css2?family=Francois+One&family=Jura:wght@400;500&family=Arimo:wght@400;700&display=swap">
<style>
  :root {
    --olive: #8a8a72;
    --olive-dark: #75755f;
    --olive-pale: #d4d6c3;
    --sage: #c3c3a2;
    --ink: #111111;
    --text-dark: #2a2a26;
    --white: #ffffff;
    --edge: #3a3a36;
    --bg-start: #050505;
    --bg-mid: #7a7a7a;
    --bg-end: #e6e6e6;
    --photo-top: #5f86b8;
    --photo-bottom: #9c8556;
  }
  * { margin: 0; padding: 0; box-sizing: border-box; }
  html, body { width: 1200px; height: 700px; overflow: hidden; }
  body {
    position: relative;
    background: linear-gradient(100deg, var(--bg-start) 0%, var(--bg-mid) 45%, var(--bg-end) 100%);
    font-family: "Arimo", Arial, sans-serif;
  }
  .card { position: absolute; overflow: hidden; }

  /* Front faces */
  .front { width: 443px; height: 254px; }
  .front-light { left: 120px; top: 38px; background: var(--olive); border-left: 4px solid var(--olive); }
  .front-olive { left: 120px; top: 370px; height: 251px; background: var(--olive-pale); border-left: 4px solid var(--olive-pale); }

  .brand-panel {
    position: absolute; top: 0; bottom: 0; left: 0; width: 198px;
    border-right: 3px dotted var(--edge);
  }
  .front-light .brand-panel { background: var(--white); }
  .front-olive .brand-panel { background: var(--olive); }

  .photo {
    position: absolute; left: 28px; width: 146px; height: 96px;
    background: linear-gradient(180deg, var(--photo-top) 0%, #8a8c84 50%, var(--photo-bottom) 100%);
  }
  .front-light .photo { top: 52px; }
  .front-olive .photo { top: 47px; left: 27px; }

  .brand-name {
    position: absolute; left: 0; width: 198px; text-align: center; white-space: nowrap;
    font-family: "Jura", sans-serif; font-weight: 500; font-size: 19px; letter-spacing: 0.8px;
  }
  .front-light .brand-name { top: 174px; color: var(--olive); }
  .front-olive .brand-name { top: 189px; color: var(--white); }

  .details { position: absolute; right: 6px; text-align: right; }
  .front-light .details { top: 12px; }
  .front-olive .details { top: 20px; }
  .holder-name {
    font-family: "Francois One", sans-serif; font-size: 19px; letter-spacing: 0.4px; white-space: nowrap;
  }
  .front-light .holder-name { color: var(--white); }
  .front-olive .holder-name { color: var(--olive); }
  .role {
    margin-right: 7px; font-size: 12.5px; color: var(--text-dark); white-space: nowrap;
  }
  .front-light .role { margin-top: 5px; line-height: 14px; }
  .front-olive .role { margin-top: 2px; line-height: 12.5px; font-weight: 700; color: var(--ink); }
  .role span { display: block; }
  .role .amp { margin-right: 4px; }

  .contact {
    position: absolute; right: 10px; text-align: right; white-space: nowrap;
    font-size: 11px; color: var(--text-dark); line-height: 1;
  }
  .front-olive .contact { color: var(--ink); }
  .front-light .contact.email { top: 174px; }
  .front-light .contact.phone { top: 199px; }
  .front-olive .contact.email { top: 190px; }
  .front-olive .contact.phone { top: 215px; }

  /* Back faces */
  .back { border: 1px solid #4a4a40; }
  .back-olive {
    left: 671px; top: 37px; width: 447px; height: 255px;
    background: radial-gradient(circle at 40% 40%, #7c7c66, var(--olive-dark));
  }
  .back-sage {
    left: 672px; top: 372px; width: 447px; height: 250px;
    background: radial-gradient(circle at 40% 40%, #c9c9aa, var(--sage));
    border-color: #222;
  }
  .back-name {
    position: absolute; font-family: "Francois One", sans-serif; font-size: 29px;
    color: var(--ink); letter-spacing: 0.6px; white-space: nowrap;
  }
  .back-olive .back-name { left: 43px; top: 88px; }
  .back-sage .back-name { left: 47px; top: 72px; }
  .back-role { position: absolute; font-size: 16px; line-height: 17px; color: #1f1f1b; white-space: nowrap; }
  .back-olive .back-role { left: 43px; top: 137px; font-family: "Jura", sans-serif; font-weight: 500; }
  .back-sage .back-role {
    left: 47px; top: 115px; font-family: "Francois One", sans-serif; font-size: 16px;
    text-shadow: 1px 1px 1px rgba(0,0,0,0.45);
  }
  .back-role span { display: block; }
</style>
</head>
<body>

  <section class="card front front-light">
    <div class="brand-panel">
      <div class="photo" role="img" aria-label="Photo of a runner on a hillside"></div>
      <div class="brand-name">Tall Oak Fitness</div>
    </div>
    <div class="details">
      <div class="holder-name">Celia R. Dunhill(BHK)</div>
      <div class="role">
        <span>Clinical Exercise Specialist</span>
        <span class="amp">&amp;</span>
        <span>Personal Trainer</span>
        <span>NBEP Certified</span>
      </div>
    </div>
    <div class="contact email">celia.dunhill@talloakfitness.example</div>
    <div class="contact phone">Call:604-358-4170</div>
  </section>

  <section class="card back back-olive">
    <div class="back-name">Celia R. Dunhill(BHK)</div>
    <div class="back-role">
      <span>Clinical Exercise Specialist &amp; Personal Trainer</span>
      <span>NBEP Certified</span>
    </div>
  </section>

  <section class="card front front-olive">
    <div class="brand-panel">
      <div class="photo" role="img" aria-label="Photo of a runner on a hillside"></div>
      <div class="brand-name">Tall Oak Fitness</div>
    </div>
    <div class="details">
      <div class="holder-name">Celia R. Dunhill(BHK)</div>
      <div class="role">
        <span>Clinical Exercise Specialist</span>
        <span class="amp">&amp;</span>
        <span>Personal Trainer</span>
        <span>NBEP Certified</span>
      </div>
    </div>
    <div class="contact email">celia.dunhill@talloakfitness.example</div>
    <div class="contact phone">Call:604-358-4170</div>
  </section>

  <section class="card back back-sage">
    <div class="back-name">Celia R. Dunhill(BHK)</div>
    <div class="back-role">
      <span>Clinical Exercise Specialist &amp; Personal Trainer</span>
      <span>NBEP Certified</span>
    </div>
  </section>

</body>
</html>
```